依頼詳細
❏デザイン依頼
・テ−マカラ−:黄緑。おだやか系の頂点。さわやかやあたらしい気持ちなどの意味がある
・作りたいイメ−ジ:とても明るく、幸せを感じる体質つくりのお手伝い。
会いたいとおもってもらう雰囲気

☆リッチメニューのデザインの狙い
・人柄を全面にだし、講座への参加の流れをつくる。

❏依頼詳細
<作成物>
■リッチメッセージ
リッチメニュー
合計2枚

〈リッチメニューの項目〉
下の段左から右へ①〜③
下の段左から右へ④〜⑤

〈リッチメニューの表示名〉
①自己紹介/HP/SNS ②講座のご案内   ③お客様の声
④なるほど情報   ⑤お楽しみ     ⑥予約・問い合わせ

デザイン重視でここの表示名はデザイン的に英語の方がよければ
英語でも大丈夫です。意味がわかって
ニュアンスがあっていれば文字を短くするのも
お任せします。あくまでデザイン重視です。

〈画像はこちらから〉
↓ソラボックスリンク
https://7.sorabox-dl.jp/0422-a3f1e9b07d52c846e0d3a71f5b92c684

※こちらの作成以外に勝手に使用された場合は
著作権侵害で法的手段をとらせていただきます。
作成事例にもしようしないでください。

<サイズ>
・リッチメッセージ(1040×1040ピクセル)
・リッチメニュー(1200×810ピクセル)

<納品形式>
・ai形式(イラストレーターデータ)
・JPG
記載項目
キャッチコピ−
自分力発見ナビゲ−タ−
サイズ
• ・リッチメッセージ(1040×1040ピクセル) ・リッチメニュー(1200×810ピクセル)
希望イメージ
シンプル 複雑
単色 カラフル
暗い 明るい
日常 高級
遊び心 厳粛
未来的 伝統的
女性的 男性的
希望する色
黄・オレンジ系、緑系
納品ファイル
• 高解像度JPG (.jpg)
• イラストレーター形式 (.ai)
補足説明
■ 選んだ理由

依頼にフィットした提案でした。

■ 提案者全員のお礼・コメント

様々な素敵な提案ありがとうございました。
次回も是非ご応募ください。

```html
<!DOCTYPE html>
<html lang="ja">
<head>
<meta charset="utf-8">
<title>色（＝個性）で輝ける人のお手伝い！ リッチメニュー</title>
<link href="https://fonts.googleapis.com/css2?family=M+PLUS+Rounded+1c:wght@500;700;800&display=swap" rel="stylesheet">
<style>
  :root {
    --cream: #fdfae0;
    --cream-deep: #f7f2c4;
    --leaf: #7dd94f;
    --leaf-dark: #5fb83a;
    --ribbon-fold: #4a9a2b;
    --grid-bg: #f4f9ec;
    --title-green: #55a92c;
    --accent-red: #e8383d;
    --accent-orange: #f0801f;
    --ink: #333333;
    --white: #ffffff;
  }
  * { box-sizing: border-box; margin: 0; padding: 0; }
  html, body { width: 716px; height: 1200px; overflow: hidden; }
  body {
    font-family: "M PLUS Rounded 1c", sans-serif;
    background: var(--white);
    color: var(--ink);
  }
  .menu { position: relative; width: 716px; height: 1200px; overflow: hidden; }

  /* upper visual area */
  .hero {
    position: absolute; left: 0; top: 0; width: 716px; height: 720px; overflow: hidden;
    background:
      radial-gradient(ellipse 420px 260px at 160px 330px, rgba(200,235,160,.45), transparent 70%),
      radial-gradient(ellipse 380px 240px at 560px 380px, rgba(255,240,170,.6), transparent 70%),
      linear-gradient(180deg, var(--cream) 0%, var(--cream-deep) 100%);
  }
  .headline {
    position: absolute; left: 26px; top: 20px; z-index: 3;
    color: var(--title-green); font-weight: 800; line-height: 1.35;
    white-space: nowrap;
  }
  .headline span {
    display: inline-block; border-bottom: 3px solid var(--title-green);
    padding-bottom: 2px;
  }
  .headline .line-1 { font-size: 32px; }
  .headline .line-2 { font-size: 36px; margin-top: 4px; }

  .pencils-photo {
    position: absolute; left: 470px; top: -40px; width: 300px; height: 170px;
    transform: rotate(-14deg);
    background: linear-gradient(90deg, #f3a24a, #e84a4a, #d85fa8, #7f6cc9, #4aa0e0, #5cc46a, #c9d94a, #f2d04a);
    opacity: .85;
  }
  .pencils-caption {
    position: absolute; left: 446px; top: 28px; width: 280px; z-index: 2;
    transform: rotate(-13deg);
    color: var(--accent-red); font-weight: 700; font-size: 16px; line-height: 1.35;
    text-align: center; white-space: nowrap;
  }

  .color-chart {
    position: absolute; left: 240px; top: 206px; width: 236px; height: 236px;
    border-radius: 50%;
    background: radial-gradient(circle, #ffffff 0%, #f6f6f0 60%, #e6e6dc 100%);
    border: 3px solid #8a8a80;
  }

  .message-ribbon { position: absolute; left: 400px; top: 224px; width: 316px; height: 130px; z-index: 2; }
  .message-ribbon p {
    position: absolute; left: 50px; top: 20px; width: 260px;
    transform: rotate(-8deg);
    color: var(--white); font-weight: 700; font-size: 16px; line-height: 1.55;
    text-align: center; white-space: nowrap;
  }

  .portrait {
    position: absolute; left: 0; top: 216px; width: 240px; height: 504px;
    background: linear-gradient(180deg, #f6e7d2 0%, #e8b7a6 45%, #d98a8a 100%);
    border-radius: 0 120px 0 0;
  }

  .name-card {
    position: absolute; left: 18px; top: 630px; width: 236px; z-index: 2;
    border-radius: 6px; overflow: hidden; box-shadow: 0 2px 4px rgba(0,0,0,.15);
  }
  .name-card .roles {
    background: var(--leaf-dark); color: var(--white);
    font-size: 11px; font-weight: 700; line-height: 1.45; padding: 4px 8px;
  }
  .name-card .person {
    background: var(--white); color: var(--ink);
    font-size: 22px; font-weight: 800; padding: 2px 10px 4px; letter-spacing: 2px;
  }

  .method {
    position: absolute; left: 262px; top: 488px; z-index: 2;
    color: var(--accent-orange); font-weight: 800; font-size: 31px;
    white-space: nowrap;
  }

  .cards-photo {
    position: absolute; left: 346px; top: 550px; width: 370px; height: 170px;
    background: linear-gradient(135deg, #d9d4c6 0%, #b9b2a2 50%, #8f8a80 100%);
  }
  .cards-caption {
    position: absolute; left: 380px; top: 630px; z-index: 2;
    transform: rotate(-12deg);
    background: rgba(255,255,255,.9); color: var(--title-green);
    font-weight: 800; font-size: 15px; line-height: 1.3; padding: 4px 10px; border-radius: 4px;
    text-align: center; white-space: nowrap;
  }

  /* lower tile grid */
  .tile-grid {
    position: absolute; left: 0; top: 720px; width: 716px; height: 480px;
    background: var(--grid-bg);
    display: grid; grid-template-columns: repeat(3, 214px); grid-template-rows: repeat(2, 222px);
    column-gap: 19px; row-gap: 16px; padding: 10px 18px 0;
  }
  .tile {
    background: var(--leaf); color: var(--white);
    display: flex; flex-direction: column; align-items: center; justify-content: center;
    gap: 12px; text-align: center; font-weight: 800;
  }
  .tile svg { width: 74px; height: 74px; }
  .tile .label { font-size: 19px; line-height: 1.3; }
  .tile .label-top { font-size: 19px; }
</style>
</head>
<body>
<div class="menu">
  <section class="hero">
    <div class="pencils-photo" role="img" aria-label="色とりどりの色鉛筆を並べた写真"></div>
    <p class="pencils-caption">誰でも色で分析力<br>コミュニケーション力が学べる</p>

    <h1 class="headline">
      <span class="line-1">色（＝個性）で</span><br>
      <span class="line-2">輝ける人のお手伝い！</span>
    </h1>

    <div class="portrait" role="img" aria-label="講師のポートレート写真"></div>

    <div class="color-chart" role="img" aria-label="カラータイプの円形チャート図"></div>

    <div class="message-ribbon">
      <svg width="316" height="130" viewBox="0 0 316 130" aria-hidden="true">
        <path d="M30 58 Q160 20 316 2 L316 86 Q170 100 52 130 Q20 96 30 58 Z" fill="var(--leaf-dark)"/>
        <path d="M30 58 L0 70 L18 86 L6 104 L52 130 Z" fill="var(--ribbon-fold)"/>
      </svg>
      <p>考え方を少し変えるだけで<br>人生は180度変わります。<br>それを選択するだけです。</p>
    </div>

    <div class="name-card">
      <div class="roles">カラータイプインストラクター認定講師<br>自分力発見ナビゲーター</div>
      <div class="person">森川 遥香</div>
    </div>

    <p class="method">心理学 × カラータイプ手法</p>

    <div class="cards-photo" role="img" aria-label="テーブルに並べたカラータイプカードのワークショップ写真"></div>
    <p class="cards-caption">カラータイプ・カードで<br>ワクワクスッキリ</p>
  </section>

  <nav class="tile-grid">
    <div class="tile">
      <span class="label-top">自己紹介</span>
      <svg viewBox="0 0 74 74" aria-hidden="true" fill="none" stroke="#fff" stroke-width="4">
        <circle cx="37" cy="37" r="28"/>
        <ellipse cx="37" cy="37" rx="12" ry="28"/>
        <line x1="9" y1="37" x2="65" y2="37"/>
      </svg>
      <span class="label">HOME PAGE<br>SNS</span>
    </div>
    <div class="tile">
      <svg viewBox="0 0 74 74" aria-hidden="true" fill="none" stroke="#fff" stroke-width="4">
        <circle cx="37" cy="37" r="11"/>
        <path d="M37 6 L42 16 L53 12 L53 24 L65 27 L58 37 L65 47 L53 50 L53 62 L42 58 L37 68 L32 58 L21 62 L21 50 L9 47 L16 37 L9 27 L21 24 L21 12 L32 16 Z" stroke-linejoin="round"/>
      </svg>
      <span class="label">講座のご案内</span>
    </div>
    <div class="tile">
      <svg viewBox="0 0 74 74" aria-hidden="true" fill="#fff">
        <path d="M12 20 L24 34 L37 12 L50 34 L62 20 L58 50 L16 50 Z" fill="none" stroke="#fff" stroke-width="4" stroke-linejoin="round"/>
        <polygon points="14,58 16,63 21,63 17,66 19,71 14,68 9,71 11,66 7,63 12,63"/>
        <polygon points="37,58 39,63 44,63 40,66 42,71 37,68 32,71 34,66 30,63 35,63"/>
        <polygon points="60,58 62,63 67,63 63,66 65,71 60,68 55,71 57,66 53,63 58,63"/>
      </svg>
      <span class="label">お客様の声</span>
    </div>
    <div class="tile">
      <svg viewBox="0 0 74 74" aria-hidden="true" fill="none" stroke="#fff" stroke-width="4">
        <path d="M37 8 A20 20 0 0 1 49 44 L49 52 L25 52 L25 44 A20 20 0 0 1 37 8 Z" fill="#fff"/>
        <line x1="27" y1="59" x2="47" y2="59"/>
        <line x1="30" y1="66" x2="44" y2="66"/>
      </svg>
      <span class="label">なるほど情報</span>
    </div>
    <div class="tile">
      <svg viewBox="0 0 74 74" aria-hidden="true" fill="none" stroke="#fff" stroke-width="4" stroke-linejoin="round">
        <rect x="10" y="26" width="54" height="12"/>
        <rect x="14" y="38" width="46" height="28"/>
        <line x1="37" y1="26" x2="37" y2="66"/>
        <path d="M37 26 C28 10 16 16 24 26 M37 26 C46 10 58 16 50 26"/>
      </svg>
      <span class="label">お楽しみ</span>
    </div>
    <div class="tile">
      <svg viewBox="0 0 74 74" aria-hidden="true" fill="#fff">
        <rect x="8" y="14" width="58" height="52" rx="4" fill="none" stroke="#fff" stroke-width="4"/>
        <rect x="8" y="14" width="58" height="12"/>
        <rect x="19" y="6" width="5" height="14" rx="2"/>
        <rect x="50" y="6" width="5" height="14" rx="2"/>
        <rect x="16" y="32" width="8" height="7"/><rect x="29" y="32" width="8" height="7"/><rect x="42" y="32" width="8" height="7"/><rect x="55" y="32" width="6" height="7"/>
        <rect x="16" y="44" width="8" height="7"/><rect x="29" y="44" width="8" height="7"/><rect x="42" y="44" width="8" height="7"/><rect x="55" y="44" width="6" height="7"/>
        <rect x="16" y="55" width="8" height="6"/><rect x="29" y="55" width="8" height="6"/>
      </svg>
      <span class="label">ご予約・問い合わせ</span>
    </div>
  </nav>
</div>
</body>
</html>
```